Brisbane IT support business needs our first business card

Hello we are a Brisbane based Information Technology company providing support and services to small and medium sized businesses. We provide a range of services and solutions.

The business name is Wattlebrook Network Computing Services, or WNCS for short.

I am looking for a business card that looks professional (don't we all want that), but most importantly, it most utilize the colours in the logo attached.

Reason: Launched late, extending so people have enough time to actually submit something.

Target Market(s)

Other business owners seeking our IT services, and also home users.

Industry/Entity Type

Business

Requirements
Must have
• Please only use the blue/orange colours in logo attached

```html
<!DOCTYPE html>
<html lang="en">
<head>
<meta charset="utf-8">
<title>WNCS Business Card</title>
<link rel="stylesheet" href="https://fonts.googleapis.com/css2?family=Lato:wght@400;700;900&display=swap">
<style>
  :root {
    --stage: #2c2c2c;
    --card-white: #f7f8f8;
    --brand-blue: #0d4a63;
    --brand-orange: #e07a23;
    --soft-white: #e4ecef;
  }
  * { box-sizing: border-box; margin: 0; padding: 0; }
  html, body { width: 1200px; height: 997px; overflow: hidden; }
  body { background: var(--stage); font-family: "Lato", Arial, sans-serif; position: relative; }

  .card {
    position: absolute;
    width: 560px;
    height: 320px;
    border-radius: 22px;
    background: var(--card-white);
    overflow: hidden;
    box-shadow: 0 18px 40px rgba(0,0,0,0.55);
  }
  .card--front { left: 80px; top: 90px; }
  .card--back { left: 560px; top: 520px; }

  .brand { position: absolute; display: flex; align-items: center; }
  .brand__dot { width: 124px; height: 124px; border-radius: 50%; background: var(--brand-blue); }
  .brand__rule { width: 3px; height: 110px; background: var(--brand-orange); margin: 0 20px 0 26px; }
  .brand__name { font-weight: 900; font-size: 66px; line-height: 1; color: var(--brand-orange); letter-spacing: 1px; }
  .brand__full {
    font-weight: 700; font-size: 12px; line-height: 1.2; color: var(--brand-blue);
    text-transform: uppercase; letter-spacing: 0.5px; margin-top: 4px; width: 200px;
  }
  .card--front .brand { left: 70px; top: 98px; }
  .card--back .brand { left: 70px; top: 28px; }

  .stripe { position: absolute; left: 0; right: 0; height: 3px; background: var(--brand-blue); }
  .stripe--one { top: 176px; }
  .stripe--two { top: 184px; }
  .band { position: absolute; left: 0; right: 0; top: 194px; bottom: 0; background: var(--brand-blue); }

  .holder { position: absolute; left: 40px; top: 252px; color: var(--soft-white); }
  .holder__name { font-weight: 900; font-size: 22px; }
  .holder__role { font-weight: 700; font-size: 14px; text-transform: uppercase; letter-spacing: 0.5px; }

  .contact { position: absolute; left: 330px; top: 206px; color: var(--soft-white); list-style: none; }
  .contact__item { display: flex; align-items: center; font-size: 14px; height: 24px; }
  .contact__icon {
    width: 18px; height: 18px; border-radius: 3px; background: var(--brand-orange);
    margin-right: 9px; display: flex; align-items: center; justify-content: center;
  }
  .contact__web { font-weight: 900; font-size: 15px; margin-top: 6px; padding-left: 4px; }
</style>
</head>
<body>
  <section class="card card--front" aria-label="Card front">
    <div class="brand">
      <div class="brand__dot"></div>
      <div class="brand__rule"></div>
      <div>
        <div class="brand__name">WNCS</div>
        <div class="brand__full">Wattlebrook Network Computing Services</div>
      </div>
    </div>
  </section>

  <section class="card card--back" aria-label="Card back">
    <div class="brand">
      <div class="brand__dot"></div>
      <div class="brand__rule"></div>
      <div>
        <div class="brand__name">WNCS</div>
        <div class="brand__full">Wattlebrook Network Computing Services</div>
      </div>
    </div>
    <div class="stripe stripe--one"></div>
    <div class="stripe stripe--two"></div>
    <div class="band"></div>

    <div class="holder">
      <p class="holder__name">Dana Whitlow</p>
      <p class="holder__role">Founder/CEO</p>
    </div>

    <ul class="contact">
      <li class="contact__item">
        <span class="contact__icon"><svg width="12" height="12" viewBox="0 0 12 12"><path d="M2 1h2.5l1 2.5-1.5 1a6 6 0 0 0 3.5 3.5l1-1.5L11 7.5V10a1 1 0 0 1-1 1A9 9 0 0 1 1 2a1 1 0 0 1 1-1z" fill="#fff"/></svg></span>
        07 3184 5520
      </li>
      <li class="contact__item">
        <span class="contact__icon"><svg width="12" height="12" viewBox="0 0 12 12"><rect x="3" y="1" width="6" height="3" fill="#fff"/><rect x="1" y="4.5" width="10" height="4.5" rx="1" fill="#fff"/><rect x="3" y="8" width="6" height="3" fill="#fff" stroke="#e07a23" stroke-width="0.8"/></svg></span>
        07 3184 5521
      </li>
      <li class="contact__item">
        <span class="contact__icon"><svg width="12" height="12" viewBox="0 0 12 12"><rect x="1" y="2.5" width="10" height="7" fill="#fff"/><path d="M1 2.5l5 4 5-4" fill="none" stroke="#e07a23" stroke-width="1"/></svg></span>
        dana@wncsolutions.com.au
      </li>
      <li class="contact__item contact__web">www.wncsolutions.com.au</li>
    </ul>
  </section>
</body>
</html>
```